Update the A4 Specials Page for Restaurant/Cafe

Provide a MINIMALIST attractive Specials page we can print weekly for our food and drink specials to give to our guests. Final design is to be provided in WORD Document so it can be easily edited by Manager. Should be black text and MINIMALIST to minimise ink usage as we print hundreds a week. We have UPLOADED the existing page as a template for you to update. Maybe logo can stay, see what you think. Or delete it and do something else. Keep it simple. Choose a good FONT. Could be a little playful with a cocktail ICON or something. Our existing menus can be seen at www.tallpinebistro.com.au and they are using font Alegreya. Please note we are unable to provide any feedback to designers, however we really do appreciate your time if you are submitting a design. Thank you for your participation.

```html
<!DOCTYPE html>
<html lang="en">
<head>
<meta charset="utf-8">
<title>Weekly Special – Tall Pine Bistro</title>
<link rel="stylesheet" href="https://fonts.googleapis.com/css2?family=Alegreya:wght@700&family=Inter:wght@300;700&display=swap">
<style>
  :root {
    --ink: #111111;
    --muted: #5a5a5a;
    --paper: #ffffff;
    --art-tone: #d9d9d9;
    --art-tone-light: #ececec;
  }
  * { margin: 0; padding: 0; box-sizing: border-box; }
  html, body { width: 849px; height: 1200px; overflow: hidden; background: var(--paper); }
  .page { position: relative; width: 849px; height: 1200px; color: var(--ink); font-family: "Inter", Arial, sans-serif; }
  .frame { position: absolute; inset: 0; }
  .line { position: absolute; left: 0; right: 0; text-align: center; white-space: nowrap; }
  .section-title { font-family: "Alegreya", Georgia, serif; font-weight: 700; }
  .page-title { top: 62px; line-height: 46px; font-size: 36px; letter-spacing: 7px; }
  .script-title { font-size: 40px; line-height: 48px; letter-spacing: 5px; }
  .item-name { font-weight: 700; font-size: 24px; line-height: 30px; }
  .item-desc { font-weight: 300; font-size: 21px; line-height: 28px; color: var(--muted); }
  .item-note { font-weight: 300; font-size: 17px; line-height: 22px; color: var(--muted); }
  .price { font-weight: 700; font-size: 27px; line-height: 32px; }
  .beer-block .line { left: -16px; }
  .art { position: absolute; border-radius: 10px; background: linear-gradient(160deg, var(--art-tone-light), var(--art-tone)); }
  .brand-box { position: absolute; left: 337px; top: 1080px; width: 177px; height: 91px; background: var(--paper); border: 3px solid var(--ink); display: flex; flex-direction: column; align-items: center; justify-content: center; }
  .brand-name { font-family: "Inter", Arial, sans-serif; font-weight: 700; font-size: 19px; line-height: 24px; text-align: center; color: var(--ink); }
</style>
</head>
<body>
<div class="page">
  <svg class="frame" width="849" height="1200" viewBox="0 0 849 1200" aria-hidden="true">
    <rect x="39" y="38" width="772" height="1099" fill="none" stroke="var(--ink)" stroke-width="1.4" stroke-dasharray="4 2"/>
    <rect x="42" y="41" width="766" height="1093" fill="none" stroke="var(--ink)" stroke-width="1.4" stroke-dasharray="4 2"/>
  </svg>

  <h1 class="line section-title page-title">WEEKLY SPECIAL</h1>
  <div class="art" style="left:191px;top:118px;width:469px;height:86px;" role="img" aria-label="Illustration of kitchen utensils and pans hanging from a rail"></div>

  <section class="food-block">
    <h2 class="line item-name" style="top:254px;">CHICKEN FILO</h2>
    <p class="line item-desc" style="top:287px;">Creamy Chicken with Pinenuts, wrapped in Filo Pastry.</p>
    <p class="line item-desc" style="top:318px;">Served with Side Salad &amp; Zulu Sauce</p>
    <p class="line price" style="top:354px;">$24</p>
    <h2 class="line item-name" style="top:397px;">MINESTRONE SOUP</h2>
    <p class="line item-desc" style="top:430px;">Served with Garlic Bread</p>
    <p class="line price" style="top:466px;">$8</p>
  </section>
  <div class="art" style="left:58px;top:322px;width:115px;height:202px;" role="img" aria-label="Illustration of a salad bowl with vegetables tossed above it"></div>

  <section class="cocktail-block">
    <h2 class="line section-title script-title" style="top:544px;">Cocktail Special</h2>
    <h3 class="line item-name" style="top:599px;">PASSIONISTA</h3>
    <p class="line item-desc" style="top:632px;">Vodka, Passionfruit Pulp, Mango Puree</p>
    <p class="line item-desc" style="top:663px;">Top up with Ginger &amp; Lemon Kombucha</p>
    <p class="line price" style="top:699px;">$17</p>
  </section>
  <div class="art" style="left:710px;top:542px;width:76px;height:160px;" role="img" aria-label="Illustration of a tall cocktail glass with straws, mint and citrus"></div>

  <section class="beer-block">
    <h2 class="line section-title script-title" style="top:796px;left:0;">Craft Beer Special</h2>
    <h3 class="line item-name" style="top:848px;">SLY GECKO</h3>
    <h3 class="line item-name" style="top:889px;">CITRUS BURST</h3>
    <h3 class="line item-name" style="top:929px;font-size:25px;">Tropical Pale Ale</h3>
    <p class="line item-note" style="top:965px;">4.8% Alc.</p>
    <p class="line price" style="top:998px;">$10</p>
  </section>
  <div class="art" style="left:63px;top:810px;width:94px;height:123px;" role="img" aria-label="Illustration of a frothy beer mug"></div>

  <div class="art" style="left:555px;top:990px;width:223px;height:137px;" role="img" aria-label="Hand lettering reading Bon Appetit with burst lines"></div>

  <div class="brand-box">
    <span class="brand-name">TALL PINE<br>BISTRO</span>
  </div>
</div>
</body>
</html>
```